Business Brochure Design Project

BRIGHTWATER FIELD SERVICES
Our company requires a business brochure designed, this design will be printed and emailed to prospective corporate clients to provide an understanding of our businesses services. The written content required in this brochure is attached as a word document.

DESIGN
The design needs to hold your attention and identify the company brand. An A4 portrait format will be used with a white background. Brochure pages will never be viewed side by side as most clients will recieve this as a pdf document attached to an email so considered this in your design. Colour graphics and images will be used to enhance the content and draw people in. To reflect quality, only high resolution images that are clear, sharp and in focus will be used. Please use the CMYK colour model when designing as this brochure will also be printed.

LOOK AND FEEL
The design needs to be savvy, appear uncluttered and have an attitude of a market leader. I want something that stands out in the crowd and effectively markets my businesses brand. It needs to be elegant, modern and have a corporate feel. I want something that has energy, is fresh, innovative, exciting and inviting.

FINISHED PRODUCT
All content in the photo shop design needs to be fully editable including text. Our business has a copy of photo shop CS6, so the finished product must be compatible with this version of software. Each page must contain the text “Copyright © 2013 Brightwater Field Services. All rights reserved”
Updates

Hi all

I will also be setting up a stationay project soon, if your are interested in being part of it please let me know.

Thanks

                          

I like designs that use a white background with the use of red, black and grey colours within

 

To all designers

Thanks for the great design work; I look forward to working with you all again in the future

 

Regards Marcus Henley

Industry/Entity Type

Shop

Requirements
Must have
• This design must be professional and of the highest calibre

Please use the CMYK colour model as this is the formatt by printers.

Business contact details must be clearly visible on the cover page
Should not have
• Each part of my business advertising needs to look interesting in its own right. This insures companies are intrigued to find out more about our services, who we are and what we do. Please do not design something that looks identical to my webpage site or Facebook page. Your design needs to adds value to the overall promotional impact of my business.

The design should not be based off a generic design template, it needs to be unique.

```html
<!DOCTYPE html>
<html lang="en">
<head>
<meta charset="utf-8">
<title>Brightwater Field Services – Testimonials</title>
<link rel="stylesheet" href="https://fonts.googleapis.com/css2?family=Montserrat:wght@800&family=Tinos:wght@400;700&display=swap">
<style>
  :root {
    --ink: #1f1f1f;
    --charcoal: #2b2b2d;
    --slate: #4a4a4d;
    --red: #d11f26;
    --red-deep: #9e1318;
    --paper: #ffffff;
  }
  * { margin: 0; padding: 0; box-sizing: border-box; }
  html, body { width: 849px; height: 1200px; overflow: hidden; background: var(--paper); }
  .page { position: relative; width: 849px; height: 1200px; overflow: hidden; background: var(--paper); font-family: "Tinos", "Times New Roman", serif; color: var(--ink); }
  .page-header, .page-footer { position: absolute; left: 0; width: 849px; display: block; }
  .page-header { top: 0; height: 240px; }
  .page-footer { bottom: 0; height: 230px; }
  .brand { position: absolute; top: 62px; left: 470px; width: 360px; }
  .brand-name { display: flex; align-items: center; gap: 10px; font-family: "Montserrat", Arial, sans-serif; font-weight: 800; font-size: 25px; line-height: 1.05; color: var(--charcoal); letter-spacing: 0.5px; }
  .brand-mark { width: 26px; height: 26px; background: var(--red); flex: none; }
  .brand-tagline { margin-top: 6px; font-size: 11px; font-style: italic; color: var(--red); }
  .testimonials { position: absolute; left: 50px; top: 322px; width: 770px; }
  .testimonial { margin-bottom: 58px; }
  .testimonial-title { font-size: 12.5px; font-weight: 700; color: var(--red-deep); margin-bottom: 6px; text-transform: uppercase; }
  .testimonial-body { font-size: 12.5px; line-height: 17px; text-indent: 12px; }
  .testimonial-sign { display: flex; font-size: 12px; text-transform: uppercase; margin-top: 1px; }
  .testimonial-sign span:nth-child(1) { width: 120px; }
  .testimonial-sign span:nth-child(2) { width: 150px; }
</style>
</head>
<body>
<div class="page">
  <svg class="page-header" viewBox="0 0 849 240" aria-hidden="true">
    <defs>
      <linearGradient id="headerShade" x1="0" y1="0" x2="1" y2="0">
        <stop offset="0" stop-color="#3a3a3d"/>
        <stop offset="1" stop-color="#1b1b1c"/>
      </linearGradient>
    </defs>
    <rect width="849" height="175" fill="url(#headerShade)"/>
    <path d="M0 175 C 250 185 380 120 470 40 L 849 30 L 849 175 Z" fill="var(--paper)" opacity="0.95"/>
    <path d="M0 160 C 240 175 360 110 440 38 C 380 130 230 195 0 190 Z" fill="var(--red)"/>
    <path d="M0 175 C 300 200 520 170 849 150 L 849 175 C 520 195 300 225 0 215 Z" fill="var(--paper)"/>
    <path d="M440 38 C 600 22 740 20 849 22 L 849 30 C 740 30 600 34 470 40 Z" fill="var(--red)"/>
  </svg>

  <div class="brand">
    <div class="brand-name"><span class="brand-mark"></span><span>BRIGHTWATER<br>FIELD SERVICES</span></div>
    <p class="brand-tagline">Providing Effective Project Controls and Management Solutions</p>
  </div>

  <main class="testimonials">
    <section class="testimonial">
      <h2 class="testimonial-title">Testimonials 5</h2>
      <p class="testimonial-body">I had the opportunity to work with Marcus within the Northgate LNG project in Queensland. He was a pleasure to work with, and had skills that in my experience few people possess. He was assertive, proactive and applied himself and his experience to ensure cost and project controls were clear and reporting was on time. He worked very well within the team environment and was always willing to get involved and help in many ways others couldn't. His varied experiences with in the Mining, Oil and Gas industries would be a definite asset to any company looking for an industry provider to provide on time cost and controls schedules. I would definitely recommend him and look forward to working with him again.</p>
      <p class="testimonial-sign"><span>Name</span><span>Title</span><span>Project</span></p>
    </section>
    <section class="testimonial">
      <h2 class="testimonial-title">Testimonials 6</h2>
      <p class="testimonial-body">I had the opportunity to work with Marcus within the Northgate LNG project in Queensland. He was a pleasure to work with, and had skills that in my experience few people possess. He was assertive, proactive and applied himself and his experience to ensure cost and project controls were clear and reporting was on time. He worked very well within the team environment and was always willing to get involved and help in many ways others couldn't. His varied experiences with in the Mining, Oil and Gas industries would be a definite asset to any company looking for an industry provider to provide on time cost and controls schedules. I would definitely recommend him and look forward to working with him again.</p>
      <p class="testimonial-sign"><span>Name</span><span>Title</span><span>Project</span></p>
    </section>
  </main>

  <svg class="page-footer" viewBox="0 0 849 230" aria-hidden="true">
    <path d="M0 60 C 280 150 560 150 849 40 L 849 230 L 0 230 Z" fill="var(--slate)" opacity="0.35"/>
    <path d="M0 95 C 300 170 560 160 849 70 L 849 230 L 0 230 Z" fill="var(--red)"/>
    <path d="M0 125 C 300 185 580 180 849 105 L 849 230 L 0 230 Z" fill="var(--paper)"/>
    <path d="M0 140 C 300 200 580 195 849 120 L 849 230 L 0 230 Z" fill="var(--charcoal)"/>
  </svg>
</div>
</body>
</html>
```